Corporate Design für IT-Dienstleister
Hallo Designer,
meine Entscheidung ist getroffen - es kann ja leider nur einer gewinnen.
Nochmals vielen Dank für die Einsendungen.
Schöne Grüße
Hallo zusammen,
ich möchte mich bei allen Designer noch mal für die vielen wirklich toll gelungenen und kreativen Vorschläge bedanken. Für die jetzt ausstehende Entscheidung möchte ich mir noch eine Nacht Zeit lassen - wobei ich sagen muss die noch verbliebenen Designs gefallen mir alle super.
Vielen Dank
@tivmolk
ich wurde auch per pn darauf hingewiesen und habe deshalb aussortiert :-/
@Pluvia Dm
zu #97 die Visitenkarte trifft es auf den Punkt. Sie wirkt elegant, klar und professionell sowie modern - super... Das Logo ist mir noch nicht ausdrucksstark genug. Vielleicht können Sie noch ein paar Alternativen (mit der gleichen Visitenkarte) vorschlagen? (Wenn Sie möchten, könne Sie auch gerne andere Farben verwenden!) Wie würde das Briefpapier aussehen?
Danke und wirklich gute Arbeit, bin gespannt...
Gruß wolkenbaer
ich bin mir noch nicht ganz sicher ob das richtige bisher dabei war.
Vielleicht hat jemand noch eine Idee für ein "einfaches" Logo.
Evtl. könnte man das Logo weglassen und mit dem "L" von "Brodhagen" irgendetwas anfangen???
Ich freue mich auf weitere Vorschläge
vielen Dank für die wirklich tollen bisherigen Vorschläge. Einige von diesen kommen bereits jetzt schon in die engere Auswahl.
Ich würde jetzt gerne noch einige Vorschläge sehen, die nicht auf den bisherigen Farben/Formen basieren und auch nicht unbedingt mit meinen Angaben im Briefing übereinstimmen. Welches Design würden Sie mir empfehlen oder welche Farben, Formen, Schriften etc. würden Sie für meine angebotenen Dienstleistungen verwenden?
Ich freue mich auf Ihre Vorschläge
MfG wolkenbaer
zu #79 und #80
sieht interessant aus... wie würde visitenkarte und geschäftspapier aussehen?
gruß wolkenbaer
#61 Die Visitenkarte finde ich top :-) - Allerdings habe ich teilweise die Rückmeldung bekommen dass es zu bunt wirkt (Meine Worte in quillbrankets Ohren) Vielleicht die Balken weg und dafür was schlichteres ?
#59 Das Geschäftspapier ist irgendwie noch nicht rund - Kann es mir auch nicht so richtig vorstellen, da da in der Mitte die Visitenkarte ist - und leider kein Text :-/
@tkgrafik
zu#46 und #47
Logo finde ich cool, vor allem die schwarze Visitenkarte ist mal was anderes und bleibt den Kunden nach der Übergabe in Erinnerung... Ich frage mich wie man diese "Besonderheit" beim Gschäftspapier mit überträgt? Wie würde die Rückseite der Visitenkarte aussehen?
@BLoomiqPX
zu #54, #55, #56
ich fand die Farbverteilung vorher besser (web rot, tele grün, pm blau) -
zu #55
Oben die Reiter auf der linken Seite sehen super aus. Leider auch mit der falschen Farbverteilung.
#57 und #58 sind mir zu blass
@vantrel:
vielen Dank für die vielen unterschiedlichen Ausführungen. Leider war bis jetzt noch nicht das richtige dabei!
@ BLoomiqPX:
#34 Das Logo ist super und kommt auf jeden Fall in kombi mit der Visitenkarte und dem Geschäftspapier die engere Auswahl. Schrit, Logo und Farben passen gut. Dieses Angebot ist aktuell mein Favorit!!!
#44 Gefällt mir auch sehr gut, haben Sie vielleicht noch weitere alternative Ideen von der Anordnung? Ich finde es sieht oben links bzw. mittig ein wenig leer aus! Den Balken unten finde ich super. Vielleicht könnte man auch mittig im Blatt mit Wasserzeichen arbeiten? Sieht dann aber vielleicht auch überladen aus! Mal schauen...
#45 Visitenkarte - kommt richtig gut! Nur die Anordung der Farben ist dann ja auf der Rückseite falsch rum. Würde ich mir gerne auch noch andersrum anschauen.
Danke und Gruß wolkenbaer
@BloomiqPX
zu #31, #32, #33
Das Logo gefällt mir richtig gut.
Als Slogan bitte mal mit "web.telefonie.projektmanagement" probieren und eine rundere weichere Schrift. Am besten gefällt mir #31 vor allem, weil das Logo über dem Namen steht und die gesammte Optik dann nicht so lang gezogen ist. Das macht sich dann bestimmt auch auf der Visitenkarte ganz gut. Mit den Farben - ob das IT nun blau ist oder nicht und welches Feld welche Farbe hat - müsste man noch mal schauen... Evtl. blau oben für Projektmanagement, web rot, telefonie grün - oder was meinst Du? Danke wolkenbaer
@vantrel
#28 ist ein gelungenes Logo und kommt in die engere Auswahl. Die Schrift + Logo etc. passen gut zusammen und gefallen mir.
#26 und #30
Der Würfel ist mir zu eckig, zu groß und die Symbole nicht modern genug.
@all
Vielen Dank für die bisherigen Vorschläge, die mir auch schon sehr gut gefallen.
Bisher fehlt mir bei den Logo's leider noch der Bezug zu meinem Unternehmen.
Ich biete 3 Dienstleistungen an (siehe Briefing), diese könnten ja z.B. in dem Logo durch Symbole dargestellt werden. Beispiel: 3d Würfel auf jeder Seite ein Symbol eingestanzt (@, telefonhörer, stift o.ä.)
Schönen Gruß wolkenbaer
zu #18
Die Schrift entspricht wie auch schon im ersten Entwurf genau meiner Vorstellung. Auch das Pipe-Symbol zwischen Namen und IT finde ich super. Dadurch wird das ganze ein wenig aufgelockert. Mein Name ist ja auch nicht gerade kurz :-) Bei dem Logo finde ich einfach keinen Zusammenhang mit meinen Dienstleistungen. Vielleicht den Slogan statt mit Punkten mit mittigen Punkten oder auch mit pipe's trennen!? Gruß
zu #16
Danke für die Aktualisierung. Kann die Schrift noch etwas weicher gestaltet werden? Und dann vielleicht im direkten Vergleich mit dem "alten" Slogan? Danke
zu #7, #8, #9, #10, #14, #15, #17
Danke für die vielen Vorschläge. Bisher ist leider noch nicht das richtige dabei. Die eingereichten Vorschläge sind mir eher noch zu einfach und nicht ausdrucksstark genug.
zu #12 und #13
Das Logo von #12 ist interessant und hat einen guten Wiedererkennungswert. Es sieht dynamisch aus. Farben sind auch gut. Evtl. den Namen auch mit großem Anfangsbuchstaben L und den Slogan wie bei #13.
zu #6 und #5
Ich finde auf dem Geschäftspapier den senkrechten Strich auf der linken Seite gut.
Das Logo sieht mir zu sehr nach CD Rom o.ä. aus. Da ich kein "PC-Schrauber" bin möchte ich keine EDV Komponenten in dem Logo haben. Die Schrift und die Farbe wirken (in Kombination) eher kalt. Ich will einen freundlichen Eindruck bei meinen Kunden hinterlassen.
zu #3
mit den 3 Symbolen hinter dem Namen kann ich leider nichts anfangen. Mir fehlt dadurch auch der Wiedererkennungswert. Die Farben sind mir zu stark. Das Logo wirkt insgesamt nicht innovativ genug.
zu #1
Das Design gefällt mir gut und geht auf jeden Fall in die richtige Richtung.
Die Farbauswahl sowie der Aufbau ist entspricht meinen Vorstellungen.
Die Ringe sind noch nicht das richtige Motiv.
Der Slogan web.telefonie.projektmanagement ist super. :-)
Vielleicht würde es auch ganz gut aussehen, wenn das Motiv über dem Namen steht, dann zieht sich das ganze nicht so in die Länge!?
wie von zurhalwig schon richtig interpretiert, bin ich auf der Suche nach einem neuen CI.
Daher bitte nicht die Farben o.ä. von meiner bisherigen Webseite übernehmen.
Von den Farben her stelle ich mir - wie in der Auftragsbeschreibung angegeben - eher etwas schlicht gehaltenes vor. Gruß wolkenbaer

```html
<!DOCTYPE html>
<html lang="de">
<head>
<meta charset="utf-8">
<title>Brodhagen IT – Briefpapier</title>
<link href="https://fonts.googleapis.com/css2?family=PT+Sans+Narrow:wght@400;700&family=Kaushan+Script&display=swap" rel="stylesheet">
<style>
  :root {
    --paper: #ffffff;
    --brand-blue: #2aa5dc;
    --brand-blue-light: #a9dcf3;
    --text-grey: #5f5f5f;
    --body-ink: #2b2b2b;
    --sign-ink: #1a1a1a;
  }
  * { margin: 0; padding: 0; box-sizing: border-box; }
  html, body { width: 874px; height: 1200px; overflow: hidden; background: var(--paper); }
  .letterhead {
    position: relative;
    width: 874px; height: 1200px;
    background: var(--paper);
    font-family: "PT Sans Narrow", "Arial Narrow", sans-serif;
    color: var(--body-ink);
  }
  .edge-motif {
    position: absolute; left: 0; top: 0;
    width: 115px; height: 400px;
    background: linear-gradient(90deg, var(--brand-blue) 0%, var(--brand-blue-light) 60%, rgba(169,220,243,0) 100%);
  }
  .brand {
    position: absolute; left: 462px; top: 52px;
    display: flex; align-items: center; gap: 18px;
  }
  .brand-name {
    font-weight: 700; font-size: 33px; letter-spacing: 3px;
    color: var(--brand-blue); line-height: 1;
  }
  .brand-mark {
    width: 40px; height: 40px; background: var(--brand-blue);
  }
  .brand-tagline {
    position: absolute; left: 464px; top: 94px;
    font-size: 13px; letter-spacing: 2.2px; color: var(--text-grey);
  }
  .sender {
    position: absolute; left: 626px; top: 172px;
    font-size: 12.5px; line-height: 19px; color: var(--text-grey);
    list-style: none;
  }
  .sender .label { color: var(--brand-blue); display: inline-block; width: 12px; }
  .sender .gap { margin-top: 6px; }
  .letter-body {
    position: absolute; left: 129px; top: 452px; width: 695px;
    font-size: 13.6px; line-height: 20.8px;
  }
  .letter-body p { margin-bottom: 20px; }
  .letter-body p.tight { margin-bottom: 0; }
  .salutation { margin-bottom: 20px; }
  .closing { margin-top: 2px; margin-bottom: 6px; }
  .signature {
    font-family: "Kaushan Script", cursive;
    font-size: 26px; color: var(--sign-ink); line-height: 1.2;
  }
</style>
</head>
<body>
<main class="letterhead">
  <div class="edge-motif" role="img" aria-label="Dekoratives blaues Wellenmotiv am linken Blattrand"></div>

  <header>
    <div class="brand">
      <span class="brand-name">BRODHAGEN IT</span>
      <span class="brand-mark"></span>
    </div>
    <div class="brand-tagline">WEB | TELEFONIE | PROJEKTMANAGEMENT</div>
  </header>

  <ul class="sender">
    <li>Jorin Brodhagen</li>
    <li>Lindenkamp 4</li>
    <li>23911 Mölnhof</li>
    <li class="gap"><span class="label">T</span> +49.(0)5678 . 214 30 61</li>
    <li><span class="label">F</span> +49.(0)5678 . 214 30 62</li>
    <li><span class="label">M</span> +49.(0)160 . 48 27 913</li>
    <li>info@brodhagen-it.de</li>
    <li>www.brodhagen-it.de</li>
  </ul>

  <article class="letter-body">
    <p class="salutation">Sehr geehrter Kunde,</p>
    <p class="tight">Lorem ipsum dolor sit amet, consectetuer adipiscing elit. Vestibulum ante ipsum primis in faucibus orci luctus et ultrices posuere cubilia Curae; Donec gravida, ante vel ornare lacinia, orci enim porta est, eget sollicitudin lectus lectus eget lacus. Cras ac enim vel dui vestibulum suscipit. Pellentesque convallis dolor vel libero. Mauris et pede. Integer accumsan. Quisque arcu ante, cursus in, ornare quis, viverra ut, justo. Sed at turpis vitae velit euismod aliquet. Nulla sagittis condimentum ligula. Maecenas convallis dui. Nullam sapien mauris, venenatis at, fermentum at, tempus eu, urna. Quisque pretium rutrum ligula. Pellentesque et arcu. In tempus urna. Donec interdum vestibulum libero.</p>
    <p>Nulla facilisi. Curabitur lorem risus, sagittis vitae, accumsan a, iaculis id, metus. Aliquam sed erat. Morbi a mauris. Praesent a lacus vitae turpis consequat semper. Praesent a lacus vitae turpis consequat semper. Nulla facilisi. Nam consectetuer mollis dolor. Pellentesque tempor. Sed elementum, felis quis porttitor sollicitudin, augue nulla sodales sapien, sit amet posuere quam purus at lacus. Pellentesque viverra dolor non nunc. Aenean id purus. Mauris et dolor. Mauris tempus diam. Pellentesque et arcu. Integer porta. Aliquam velit dui, commodo quis, porttitor eget, convallis et, nisi. Quisque malesuada nulla sed pede volutpat pulvinar.</p>
    <p>Donec ut urna. Fusce venenatis ligula in pede. Mauris tempor ultrices justo. Maecenas viverra. Vestibulum ante ipsum primis in faucibus orci luctus et ultrices posuere cubilia Curae; Suspendisse potenti. Aenean turpis ipsum, rhoncus vitae, posuere vitae, euismod sed, ligula. Aenean luctus vulputate turpis. Donec sit amet enim. Aliquam sed erat. Aenean turpis ipsum, rhoncus vitae, posuere vitae, euismod sed, ligula. Aliquam velit dui, commodo quis, porttitor eget, convallis et, nisi. In tempus urna. Quisque aliquam, nulla ac scelerisque convallis, nisi ligula sagittis risus, at nonummy arcu urna pulvinar nibh. Vestibulum ante ipsum primis in faucibus orci luctus et ultrices posuere cubilia Curae; Vivamus eu orci. Maecenas justo. In hac habitasse platea dictumst. Mauris tincidunt aliquam ante. Sed fringilla.</p>
    <p class="closing">Mit freundlichen Grüßen</p>
    <p class="signature">Jorin Brodhagen</p>
  </article>
</main>
</body>
</html>
```